Wedding Decor and Entertianment business card

Company - We run a weddings and events company called Amber Finch, we provide most entertainment and decor services to our customers.

Initial idea is ....
A simple business card with logo on the front, this will be spot varnish. On a matt black background.
The reverse will be simple contact information.

But happy to try things outside of the box and would welcome some crazy ideas.

Target Market(s)

wedding couples - 21 - 40
High end wedding venues.

Industry/Entity Type

Wedding

Contact Information for Business Card

01492 718 263
amberfinchevents.co.uk
rowan@amberfinchevents.co.uk
or
helena@amberfinchevents.co.uk

Requirements
Nice to have
• black matt background with spot varnish logo on the front.

```html
<!DOCTYPE html>
<html lang="en">
<head>
<meta charset="utf-8">
<title>Amber Finch – Business Card</title>
<link href="https://fonts.googleapis.com/css2?family=Bebas+Neue&family=Open+Sans:wght@400;600&display=swap" rel="stylesheet">
<style>
  :root {
    --backdrop: #ece9e6;
    --card-white: #ffffff;
    --card-black: #232323;
    --varnish: #121212;
    --plum: #7b4c78;
    --ink: #1c1c1c;
    --shadow: rgba(0, 0, 0, 0.18);
  }
  * { margin: 0; padding: 0; box-sizing: border-box; }
  html, body {
    width: 1200px;
    height: 1000px;
    overflow: hidden;
    background: var(--backdrop);
  }
  .canvas {
    position: relative;
    width: 1200px;
    height: 1000px;
  }
  .card {
    position: absolute;
    left: 265px;
    width: 666px;
    height: 398px;
    border-radius: 26px;
    box-shadow: 0 6px 18px var(--shadow);
  }
  .card--contact { top: 73px; background: var(--card-white); }
  .card--brand { top: 532px; background: var(--card-black); }

  .identity {
    position: absolute;
    right: calc(666px - 310px);
    top: 163px;
    text-align: right;
  }
  .identity__name {
    font-family: "Bebas Neue", "Arial Narrow", sans-serif;
    font-size: 44px;
    line-height: 44px;
    color: var(--plum);
    letter-spacing: 0.5px;
  }
  .identity__role {
    font-family: "Open Sans", Arial, sans-serif;
    font-size: 16px;
    line-height: 20px;
    color: var(--ink);
    margin-top: 2px;
  }
  .divider {
    position: absolute;
    left: 332px;
    top: 168px;
    width: 2px;
    height: 58px;
    background: var(--ink);
  }
  .contact-list {
    position: absolute;
    left: 352px;
    top: 162px;
    list-style: none;
  }
  .contact-list__item {
    display: flex;
    align-items: center;
    height: 23px;
    font-family: "Open Sans", Arial, sans-serif;
    font-size: 16px;
    color: var(--ink);
  }
  .contact-list__icon {
    width: 14px;
    height: 14px;
    margin-right: 10px;
    flex: none;
  }

  .wordmark {
    position: absolute;
    left: 0;
    right: 0;
    top: 176px;
    display: flex;
    justify-content: center;
    align-items: center;
    gap: 22px;
  }
  .wordmark__dot {
    width: 40px;
    height: 40px;
    border-radius: 50%;
    background: var(--varnish);
  }
  .wordmark__name {
    font-family: "Open Sans", Arial, sans-serif;
    font-weight: 400;
    font-size: 30px;
    letter-spacing: 11px;
    color: var(--varnish);
    text-transform: uppercase;
  }
</style>
</head>
<body>
<main class="canvas">
  <section class="card card--contact" aria-label="Contact side">
    <div class="identity">
      <h1 class="identity__name">Elliot Marsh</h1>
      <p class="identity__role">President</p>
    </div>
    <span class="divider"></span>
    <ul class="contact-list">
      <li class="contact-list__item">
        <svg class="contact-list__icon" viewBox="0 0 14 14" aria-hidden="true">
          <path d="M1 5 Q7 0 13 5 L11 6.5 L9.5 5 L4.5 5 L3 6.5 Z" fill="var(--plum)"/>
          <rect x="3" y="7" width="8" height="5" rx="1" fill="var(--plum)"/>
        </svg>
        01492 718 263
      </li>
      <li class="contact-list__item">
        <svg class="contact-list__icon" viewBox="0 0 14 14" aria-hidden="true">
          <rect x="1" y="3" width="12" height="8" fill="var(--plum)"/>
          <path d="M1 3 L7 8 L13 3" fill="none" stroke="#fff" stroke-width="1.2"/>
        </svg>
        helena@amberfinchevents.co.uk
      </li>
      <li class="contact-list__item">
        <svg class="contact-list__icon" viewBox="0 0 14 14" aria-hidden="true">
          <circle cx="6" cy="6" r="5" fill="none" stroke="var(--plum)" stroke-width="1.6"/>
          <path d="M7 7 L13 9 L10 10 L9 13 Z" fill="var(--plum)"/>
        </svg>
        amberfinchevents.co.uk
      </li>
    </ul>
  </section>

  <section class="card card--brand" aria-label="Brand side">
    <div class="wordmark">
      <span class="wordmark__dot"></span>
      <span class="wordmark__name">Amber Finch</span>
    </div>
  </section>
</main>
</body>
</html>
```